Restaurant service company needs a website!

I am looking for a skilled web designer/developer to create a professional, responsive, and easy-to-navigate website for my company, which specializes in servicing restaurant cooking equipment. The site should communicate trust, reliability, and technical expertise to our target audience, restaurant owners, managers, and commercial kitchen operators. I have included the company logos, if any other format for them is needed please let me know.

Target Market(s)

restaurant owners, managers, and commercial kitchen operators

Industry/Entity Type

Commercial Kitchen Equipment Service

Coding

Coded - Design and coding required

Number of Pages Required

1 page

Font styles to use
Serif
Sans Serif

Requirements
Must have
• Contact and service request forms, Click-to-call functionality for mobile, Clean, modern layout with strong visuals, Easy navigation, mobile-friendly
Nice to have
• Testimonials or Reviews, If possible a click-to-text functionality for mobile.
Should not have
• Any mention of Refrigeration or HVAC, "Free Quotes"

```html
<!DOCTYPE html>
<html lang="en">
<head>
<meta charset="utf-8">
<title>Hearthline Kitchen Service</title>
<link href="https://fonts.googleapis.com/css2?family=Figtree:wght@400;500;600&family=Inter:wght@400;500;600&display=swap" rel="stylesheet">
<style>
:root{
  --stage:#6b6b6b;
  --white:#ffffff;
  --mint:#e4f2f0;
  --teal:#137c78;
  --ink:#141a1a;
  --muted:#4a5454;
  --line:#c9d3d2;
  --steel-a:#8d9294;
  --steel-b:#3f4446;
  --head:"Figtree",sans-serif;
  --body:"Inter",sans-serif;
}
*{box-sizing:border-box;margin:0;padding:0}
html,body{width:1200px;height:4796px;overflow:hidden}
body{background:var(--stage);font-family:var(--body);color:var(--ink);position:relative}
.frame{position:absolute;top:0;background:var(--white);overflow:hidden}
.desktop{left:69px;width:783px;height:4796px}
.mobile{left:941px;width:203px;height:4796px}
section{position:relative;width:100%}
.mint{background:var(--mint)}
.center{text-align:center}
h1,h2,h3{font-family:var(--head);font-weight:400;color:var(--ink)}
.photo{background:linear-gradient(135deg,var(--steel-a),var(--steel-b));display:block}
.brand{display:flex;align-items:center;gap:4px;font-family:var(--body);font-weight:600;color:var(--teal);letter-spacing:.02em}
.brand i{display:block;background:var(--teal)}
.btn{display:inline-block;border-radius:999px;border:1px solid var(--line);background:var(--white);color:var(--ink);font-family:var(--body);font-weight:500;cursor:pointer}
.btn.primary{background:var(--teal);border-color:var(--teal);color:var(--white)}
.link{display:inline-block;color:var(--ink);font-weight:500}
.link::after{content:" ›"}
.eyebrow{font-weight:600;display:block}
.dot{display:inline-block;border-radius:50%;background:var(--ink)}
a{color:var(--ink)}

/* request form */
.request{display:grid;grid-template-columns:1fr 1fr;text-align:left}
.request label{display:block;font-weight:500;color:var(--ink)}
.request input,.request select,.request textarea{display:block;width:100%;border:1px solid var(--line);background:var(--white);color:var(--ink);font-family:var(--body);border-radius:4px}
.request textarea{resize:none}
.request .full{grid-column:1 / -1}
.request .send{grid-column:1 / -1;text-align:center}

/* ---------- Desktop ---------- */
.desktop .nav{height:37px;display:flex;align-items:center;justify-content:space-between;padding:0 32px 0 34px}
.desktop .brand{font-size:13px}
.desktop .brand i{width:9px;height:9px}
.desktop .nav ul{display:flex;list-style:none;gap:17px;align-items:center;font-size:8px}
.desktop .nav .btn{font-size:8px;padding:3px 9px}
.desktop .btn{font-size:8px;padding:4px 9px}
.desktop .link{font-size:8px;margin-left:10px}
.desktop .eyebrow{font-size:7.5px;margin-bottom:8px}
.desktop .hero{height:344px;padding-top:64px}
.desktop .hero h1{font-size:41px;line-height:46px;width:420px;margin:0 auto}
.desktop .hero p{font-size:9.5px;line-height:14px;width:420px;margin:17px auto 16px;color:var(--muted)}
.desktop .wide{height:438px}
.desktop .wide.short{height:288px}
.desktop .intro{padding-top:66px}
.desktop .intro h2{font-size:27px;line-height:32px;width:420px;margin:0 auto}
.desktop .intro p{font-size:9px;line-height:13px;width:410px;margin:14px auto 18px;color:var(--muted)}
.desktop .tabs{display:flex;justify-content:center;gap:12px;font-size:7.5px;margin-top:44px}
.desktop .tabs span.on{border-bottom:1px solid var(--teal);padding-bottom:3px}
.desktop .split{display:flex;align-items:center;justify-content:space-between;padding:0 44px 0 43px}
.desktop .split .copy{width:325px}
.desktop .split h3{font-size:24px;line-height:30px}
.desktop .split p{font-size:8.5px;line-height:12.5px;color:var(--muted);margin:12px 0 14px}
.desktop .split .photo{width:326px;height:326px;border-radius:12px}
.desktop .service{height:716px}
.desktop .service .split{margin-top:28px}
.desktop .solutions{height:508px}
.desktop .trio{display:flex;justify-content:space-between;padding:0 43px;margin-top:38px}
.desktop .trio div{width:205px;text-align:center}
.desktop .trio svg{width:18px;height:18px}
.desktop .trio h3{font-size:17px;line-height:26px;margin-top:8px}
.desktop .trio p{font-size:7.5px;line-height:11px;color:var(--muted);margin-top:10px}
.desktop .actions{margin-top:70px}
.desktop .feature{height:447px;padding-top:17px;border-top:1px solid var(--line)}
.desktop .feature .tag{font-size:8px;font-weight:600;padding-left:43px;margin-bottom:24px}
.desktop .feature .tag b{margin-right:14px}
.desktop .reviews{height:391px;padding-top:76px}
.desktop .reviews h2{font-size:27px}
.desktop .reviews > p{font-size:8.5px;color:var(--muted);margin-top:14px}
.desktop .quotes{display:flex;justify-content:space-between;padding:0 74px;margin-top:42px}
.desktop .quote{width:200px;text-align:center}
.desktop .quote .co{font-size:7px;font-weight:600}
.desktop .quote q{display:block;font-size:9px;line-height:13px;margin:14px 0 10px}
.desktop .quote .avatar{width:22px;height:22px;border-radius:50%;background:#d8dede;margin:0 auto 8px;display:block}
.desktop .quote b{font-size:7.5px;display:block}
.desktop .quote small{font-size:7px;color:var(--muted)}
.desktop .cta{height:420px;padding-top:60px}
.desktop .cta h2{font-size:27px;line-height:32px;width:420px;margin:0 auto}
.desktop .cta p{font-size:8.5px;line-height:12.5px;width:400px;margin:14px auto 20px;color:var(--muted)}
.desktop .request{width:500px;margin:0 auto;gap:9px 12px}
.desktop .request label{font-size:7px;margin-bottom:3px}
.desktop .request input,.desktop .request select{height:22px;font-size:8px;padding:0 7px}
.desktop .request textarea{height:40px;font-size:8px;padding:5px 7px}
.desktop .request .send{margin-top:4px}
.desktop footer{height:312px;padding:48px 44px 0 43px;position:relative}
.desktop footer .brand{font-size:11px}
.desktop footer .info{font-size:7px;line-height:10px;margin-top:12px}
.desktop footer .info b{display:block;margin-top:10px}
.desktop footer .info a{display:block}
.desktop .socials{display:flex;gap:6px;margin-top:10px}
.desktop .socials span{width:9px;height:9px}
.desktop .cols{position:absolute;top:48px;left:522px;display:flex;gap:40px;font-size:7px;line-height:20px;font-weight:500;list-style:none}
.desktop .cols ul{list-style:none}
.desktop .bottom{position:absolute;left:43px;right:44px;top:256px;border-top:1px solid var(--line);padding-top:10px;display:flex;justify-content:space-between;font-size:7px}
.desktop .bottom span{margin-left:14px;text-decoration:underline}

/* ---------- Mobile ---------- */
.mobile .nav{height:30px;display:flex;align-items:center;justify-content:space-between;padding:0 10px}
.mobile .brand{font-size:8px}
.mobile .brand i{width:6px;height:6px}
.mobile .nav svg{width:8px;height:8px}
.mobile .btn{font-size:5.5px;padding:3px 7px}
.mobile .link{font-size:5.5px;margin-left:7px}
.mobile .eyebrow{font-size:5.5px;margin-bottom:6px}
.mobile .hero{height:286px;padding:42px 14px 0}
.mobile .hero h1{font-size:20px;line-height:27px}
.mobile .hero p{font-size:7px;line-height:11px;margin:12px 0 14px;color:var(--muted)}
.mobile .wide{height:116px}
.mobile .service{height:712px;padding:38px 11px 0}
.mobile .service h2,.mobile .solutions h2{font-size:17px;line-height:22px}
.mobile .service .lead p,.mobile .solutions > p{font-size:6.5px;line-height:10px;color:var(--muted);margin:12px 0 16px}
.mobile .tabs{display:flex;gap:10px;font-size:5.5px;margin-top:32px}
.mobile .tabs span.on{border-bottom:1px solid var(--teal);padding-bottom:2px}
.mobile .stack h3{font-size:15px;line-height:19px}
.mobile .stack p{font-size:6.5px;line-height:10px;color:var(--muted);margin:10px 0 12px}
.mobile .stack .photo{width:182px;height:182px;border-radius:10px;margin-top:26px}
.mobile .service .stack{margin-top:34px}
.mobile .solutions{height:623px;padding:38px 11px 0}
.mobile .solutions .item{margin-top:38px}
.mobile .solutions .item:first-of-type{margin-top:26px}
.mobile .solutions svg{width:16px;height:16px}
.mobile .solutions .item h3{font-size:11px;line-height:16px;margin-top:10px}
.mobile .solutions .item p{font-size:6px;line-height:9.5px;color:var(--muted);margin-top:8px}
.mobile .solutions .actions{margin-top:30px}
.mobile .feature{height:473px;padding:13px 11px 0;border-top:1px solid var(--line)}
.mobile .feature .tag{font-size:5.5px;font-weight:600;margin-bottom:28px}
.mobile .feature .tag b{margin-right:9px}
.mobile .reviews{height:648px;padding:42px 11px 0}
.mobile .reviews h2{font-size:17px}
.mobile .reviews > p{font-size:6.5px;line-height:10px;color:var(--muted);margin-top:10px}
.mobile .quote{margin-top:32px;text-align:center}
.mobile .quote .co{font-size:5.5px;font-weight:600}
.mobile .quote q{display:block;font-size:6.5px;line-height:10px;margin:10px 0 8px}
.mobile .quote .avatar{width:16px;height:16px;border-radius:50%;background:#d8dede;margin:0 auto 6px;display:block}
.mobile .quote b{font-size:5.5px;display:block}
.mobile .quote small{font-size:5.5px;color:var(--muted)}
.mobile .cta{height:326px;padding:34px 11px 0}
.mobile .cta h2{font-size:17px;line-height:22px}
.mobile .cta p{font-size:6.5px;line-height:10px;color:var(--muted);margin:10px 0 12px}
.mobile .request{gap:6px 6px}
.mobile .request label{font-size:5px;margin-bottom:2px}
.mobile .request input,.mobile .request select{height:16px;font-size:6px;padding:0 4px}
.mobile .request textarea{height:30px;font-size:6px;padding:3px 4px}
.mobile .request .send{margin-top:3px}
.mobile .tail{height:60px}
.mobile footer{height:577px;padding:30px 11px 0}
.mobile footer .brand{font-size:8px}
.mobile footer .info{font-size:5.5px;line-height:9px;margin-top:12px}
.mobile footer .info b{display:block;margin-top:10px}
.mobile footer .info a{display:block}
.mobile .socials{display:flex;gap:5px;margin-top:8px}
.mobile .socials span{width:7px;height:7px}
.mobile footer ul{list-style:none;font-size:5.5px;line-height:20px;font-weight:500;margin-top:22px}
.mobile footer .legal{margin-top:26px;font-size:5.5px;line-height:20px;text-decoration:underline}
.mobile footer .copy{font-size:5.5px;line-height:9px;margin-top:12px;color:var(--muted)}
</style>
</head>
<body>

<div class="frame desktop">
  <header class="nav">
    <div class="brand"><i></i>HEARTHLINE</div>
    <ul>
      <li>Services</li><li>Pricing</li><li>About us</li><li>Resources ⌄</li>
      <li><span class="btn">Contact</span> <span class="btn primary">Schedule</span></li>
    </ul>
  </header>

  <section class="hero center">
    <h1>Keeping restaurant kitchens running without interruption</h1>
    <p>We provide expert restaurant equipment servicing that keeps your kitchen operational. Our technicians respond fast and fix problems before they stop your business.</p>
    <span class="btn primary">Schedule</span> <span class="btn">Learn more</span>
  </section>

  <div class="photo wide" role="img" aria-label="Photo of a clean stainless steel commercial kitchen"></div>

  <section class="service mint">
    <div class="intro center">
      <span class="eyebrow">Service</span>
      <h2>Expert restaurant equipment maintenance</h2>
      <p>We understand commercial kitchens need reliable equipment to serve customers. Our technicians are trained to diagnose and repair complex kitchen systems quickly.</p>
      <span class="btn">Contact us</span><span class="link">Learn more</span>
      <div class="tabs"><span class="on">Repair</span><span>Maintenance</span><span>Installation</span></div>
    </div>
    <div class="split">
      <div class="copy">
        <span class="eyebrow">Expertise</span>
        <h3>Professional diagnostic and repair services</h3>
        <p>Our technicians use advanced tools to identify and resolve equipment issues efficiently. We minimize downtime for your kitchen.</p>
        <span class="btn">Schedule</span><span class="link">Details</span>
      </div>
      <div class="photo" role="img" aria-label="Photo of a technician checking a clipboard beside a combi oven"></div>
    </div>
  </section>

  <section class="solutions">
    <div class="intro center">
      <span class="eyebrow">Solutions</span>
      <h2>Comprehensive restaurant equipment services</h2>
      <p>We provide tailored solutions to keep your commercial kitchen running smoothly and efficiently.</p>
    </div>
    <div class="trio">
      <div>
        <svg viewBox="0 0 20 20"><path d="M10 2l6 2.5v5c0 4-3 6.5-6 8.5-3-2-6-4.5-6-8.5v-5z" fill="none" stroke="#141a1a" stroke-width="1.6"/><circle cx="10" cy="9.5" r="2.2" fill="#141a1a"/></svg>
        <h3>Preventative maintenance programs</h3>
        <p>Regular checks to prevent unexpected equipment failures.</p>
      </div>
      <div>
        <svg viewBox="0 0 20 20"><path d="M10 2v16M3.1 6l13.8 8M3.1 14l13.8-8" stroke="#141a1a" stroke-width="2"/></svg>
        <h3>Emergency repair services</h3>
        <p>Fast response when critical kitchen equipment breaks down.</p>
      </div>
      <div>
        <svg viewBox="0 0 20 20"><rect x="3.5" y="2.5" width="13" height="15" rx="1.5" fill="none" stroke="#141a1a" stroke-width="1.6"/><path d="M3.5 7.5h13M6 5h2" stroke="#141a1a" stroke-width="1.6"/></svg>
        <h3>Equipment sales and installation</h3>
        <p>Professional setup and integration of new kitchen equipment.</p>
      </div>
    </div>
    <div class="actions center"><span class="btn">Contact us</span><span class="link">Learn more</span></div>
  </section>

  <section class="feature mint">
    <div class="tag"><b>01</b>Cost reduction</div>
    <div class="split">
      <div class="copy">
        <span class="eyebrow">Savings</span>
        <h3>Proactive maintenance saves money</h3>
        <p>Regular servicing prevents expensive breakdowns and extends equipment lifespan. We help you minimize unexpected repair costs.</p>
        <span class="btn">Calculate savings</span><span class="link">Learn more</span>
      </div>
      <div class="photo" role="img" aria-label="Photo of a technician wiring a commercial range"></div>
    </div>
  </section>
  <section class="feature mint">
    <div class="tag"><b>02</b>Kitchen efficiency</div>
    <div class="split">
      <div class="copy">
        <span class="eyebrow">Performance</span>
        <h3>Optimize kitchen equipment performance</h3>
        <p>Well-maintained equipment operates at peak efficiency, reducing energy consumption and improving overall kitchen productivity.</p>
        <span class="btn">Get assessment</span><span class="link">Explore</span>
      </div>
      <div class="photo" role="img" aria-label="Photo of a chef and technician reviewing a tablet in a kitchen"></div>
    </div>
  </section>
  <section class="feature mint">
    <div class="tag"><b>03</b>Business continuity</div>
    <div class="split">
      <div class="copy">
        <span class="eyebrow">Reliability</span>
        <h3>Minimize disruptions to your restaurant</h3>
        <p>Our rapid response and comprehensive maintenance services ensure your kitchen remains operational, protecting your business reputation.</p>
        <span class="btn">Emergency support</span><span class="link">Contact us</span>
      </div>
      <div class="photo" role="img" aria-label="Photo of a technician servicing a fryer while a manager watches"></div>
    </div>
  </section>

  <section class="reviews center">
    <h2>What our clients say</h2>
    <p>Hear from restaurant owners who trust our expert equipment maintenance services</p>
    <div class="quotes">
      <div class="quote"><span class="co">COMPANY LOGO</span><q>Their quick response saved our kitchen during a critical equipment failure.</q><span class="avatar" role="img" aria-label="Client portrait"></span><b>Marcus Bell</b><small>Head chef, Laneway Bistro</small></div>
      <div class="quote"><span class="co">COMPANY LOGO</span><q>Professional, efficient, and incredibly knowledgeable about commercial kitchen equipment.</q><span class="avatar" role="img" aria-label="Client portrait"></span><b>Elena Moreau</b><small>Operations manager, Tidewater Cafe</small></div>
      <div class="quote"><span class="co">COMPANY LOGO</span><q>We've reduced our equipment downtime by 70% since working with them.</q><span class="avatar" role="img" aria-label="Client portrait"></span><b>Daniel Park</b><small>Owner, Jade Lantern Restaurant</small></div>
    </div>
  </section>

  <section class="cta mint center" id="request">
    <h2>Ready to optimize your kitchen equipment</h2>
    <p>Contact our expert technicians for a comprehensive assessment of your restaurant's equipment maintenance needs.</p>
    <form class="request" action="#" method="post">
      <div><label for="d-name">Name</label><input id="d-name" name="name" type="text" placeholder="Your name"></div>
      <div><label for="d-phone">Phone</label><input id="d-phone" name="phone" type="tel" placeholder="Best number to call"></div>
      <div><label for="d-email">Email</label><input id="d-email" name="email" type="email" placeholder="you@restaurant.com"></div>
      <div><label for="d-type">Service needed</label>
        <select id="d-type" name="service"><option>Repair</option><option>Maintenance</option><option>Installation</option><option>Emergency support</option></select></div>
      <div class="full"><label for="d-msg">Equipment and issue</label><textarea id="d-msg" name="message" placeholder="Tell us which equipment needs attention"></textarea></div>
      <div class="send"><button class="btn primary" type="submit">Schedule service</button> <span class="btn">Get quote</span></div>
    </form>
  </section>

  <div class="photo wide short" role="img" aria-label="Photo of two technicians discussing a tablet in a commercial kitchen"></div>

  <footer>
    <div class="brand"><i></i>HEARTHLINE</div>
    <div class="info">
      <b>Address</b>Level 2, 48 Harbour Lane, Sydney NSW 2000
      <b>Contact</b><a href="tel:1800000000">1800 000 000</a><a href="mailto:hello@hearthlineservice.com">hello@hearthlineservice.com</a>
    </div>
    <div class="socials"><span class="dot"></span><span class="dot"></span><span class="dot"></span><span class="dot"></span><span class="dot"></span></div>
    <div class="cols">
      <ul><li>Services</li><li>Repair plans</li><li>Maintenance</li><li>Installation</li><li>Equipment sales</li></ul>
      <ul><li>Emergency support</li><li>About company</li><li>Our team</li><li>Careers</li><li>Contact us</li></ul>
    </div>
    <div class="bottom">
      <div>© 2024 Hearthline Kitchen Service. All rights reserved.</div>
      <div><span>Privacy policy</span><span>Terms of service</span><span>Cookies settings</span></div>
    </div>
  </footer>
</div>

<div class="frame mobile">
  <header class="nav">
    <div class="brand"><i></i>HEARTHLINE</div>
    <svg viewBox="0 0 10 10"><path d="M1 1l8 8M9 1l-8 8" stroke="#141a1a" stroke-width="1.4"/></svg>
  </header>

  <section class="hero center">
    <h1>Keeping restaurant kitchens running without interruption</h1>
    <p>We provide expert restaurant equipment servicing that keeps your kitchen operational. Our technicians respond fast and fix problems before they stop your business.</p>
    <span class="btn primary">Schedule</span> <span class="btn">Learn more</span>
  </section>

  <div class="photo wide" role="img" aria-label="Photo of a clean stainless steel commercial kitchen"></div>

  <section class="service mint">
    <div class="lead center">
      <span class="eyebrow">Service</span>
      <h2>Expert restaurant equipment maintenance</h2>
      <p>We understand commercial kitchens need reliable equipment to serve customers. Our technicians are trained to diagnose and repair complex kitchen systems quickly.</p>
      <span class="btn">Contact us</span><span class="link">Learn more</span>
    </div>
    <div class="tabs"><span class="on">Repair</span><span>Maintenance</span><span>Installation</span></div>
    <div class="stack">
      <span class="eyebrow">Expertise</span>
      <h3>Professional diagnostic and repair services</h3>
      <p>Our technicians use advanced tools to identify and resolve equipment issues efficiently. We minimize downtime for your kitchen.</p>
      <span class="btn">Schedule</span><span class="link">Details</span>
      <div class="photo" role="img" aria-label="Photo of a technician checking a clipboard beside a combi oven"></div>
    </div>
  </section>

  <section class="solutions center">
    <span class="eyebrow">Solutions</span>
    <h2>Comprehensive restaurant equipment services</h2>
    <p>We provide tailored solutions to keep your commercial kitchen running smoothly and efficiently.</p>
    <div class="item">
      <svg viewBox="0 0 20 20"><path d="M10 2l6 2.5v5c0 4-3 6.5-6 8.5-3-2-6-4.5-6-8.5v-5z" fill="none" stroke="#141a1a" stroke-width="1.6"/><circle cx="10" cy="9.5" r="2.2" fill="#141a1a"/></svg>
      <h3>Preventative maintenance programs</h3>
      <p>Regular checks to prevent unexpected equipment failures.</p>
    </div>
    <div class="item">
      <svg viewBox="0 0 20 20"><path d="M10 2v16M3.1 6l13.8 8M3.1 14l13.8-8" stroke="#141a1a" stroke-width="2"/></svg>
      <h3>Emergency repair services</h3>
      <p>Fast response when critical kitchen equipment breaks down.</p>
    </div>
    <div class="item">
      <svg viewBox="0 0 20 20"><rect x="3.5" y="2.5" width="13" height="15" rx="1.5" fill="none" stroke="#141a1a" stroke-width="1.6"/><path d="M3.5 7.5h13M6 5h2" stroke="#141a1a" stroke-width="1.6"/></svg>
      <h3>Equipment sales and installation</h3>
      <p>Professional setup and integration of new kitchen equipment.</p>
    </div>
    <div class="actions"><span class="btn">Contact us</span><span class="link">Learn more</span></div>
  </section>

  <section class="feature mint">
    <div class="tag"><b>01</b>Cost reduction</div>
    <div class="stack">
      <span class="eyebrow">Savings</span>
      <h3>Proactive maintenance saves money</h3>
      <p>Regular servicing prevents expensive breakdowns and extends equipment lifespan. We help you minimize unexpected repair costs.</p>
      <span class="btn">Calculate savings</span><span class="link">Learn more</span>
      <div class="photo" role="img" aria-label="Photo of a technician wiring a commercial range"></div>
    </div>
  </section>
  <section class="feature mint">
    <div class="tag"><b>01</b>Feature one</div>
    <div class="stack">
      <span class="eyebrow">Performance</span>
      <h3>Optimize kitchen equipment performance</h3>
      <p>Well-maintained equipment operates at peak efficiency, reducing energy consumption and improving overall kitchen productivity.</p>
      <span class="btn">Get assessment</span><span class="link">Explore</span>
      <div class="photo" role="img" aria-label="Photo of a chef and technician reviewing a tablet in a kitchen"></div>
    </div>
  </section>
  <section class="feature mint">
    <div class="tag"><b>01</b>Feature one</div>
    <div class="stack">
      <span class="eyebrow">Reliability</span>
      <h3>Minimize disruptions to your restaurant</h3>
      <p>Our rapid response and comprehensive maintenance services ensure your kitchen remains operational, protecting your business reputation.</p>
      <span class="btn">Emergency support</span><span class="link">Contact us</span>
      <div class="photo" role="img" aria-label="Photo of a technician servicing a fryer while a manager watches"></div>
    </div>
  </section>

  <section class="reviews center">
    <h2>What our clients say</h2>
    <p>Hear from restaurant owners who trust our expert equipment maintenance services</p>
    <div class="quote"><span class="co">COMPANY LOGO</span><q>Their quick response saved our kitchen during a critical equipment failure.</q><span class="avatar" role="img" aria-label="Client portrait"></span><b>Marcus Bell</b><small>Head chef, Laneway Bistro</small></div>
    <div class="quote"><span class="co">COMPANY LOGO</span><q>Professional, efficient, and incredibly knowledgeable about commercial kitchen equipment.</q><span class="avatar" role="img" aria-label="Client portrait"></span><b>Elena Moreau</b><small>Operations manager, Tidewater Cafe</small></div>
    <div class="quote"><span class="co">COMPANY LOGO</span><q>We've reduced our equipment downtime by 70% since working with them.</q><span class="avatar" role="img" aria-label="Client portrait"></span><b>Daniel Park</b><small>Owner, Jade Lantern Restaurant</small></div>
  </section>

  <section class="cta mint center">
    <h2>Ready to optimize your kitchen equipment</h2>
    <p>Contact our expert technicians for a comprehensive assessment of your restaurant's equipment maintenance needs.</p>
    <form class="request" action="#" method="post">
      <div><label for="m-name">Name</label><input id="m-name" name="name" type="text" placeholder="Your name"></div>
      <div><label for="m-phone">Phone</label><input id="m-phone" name="phone" type="tel" placeholder="Number"></div>
      <div><label for="m-email">Email</label><input id="m-email" name="email" type="email" placeholder="Email"></div>
      <div><label for="m-type">Service</label>
        <select id="m-type" name="service"><option>Repair</option><option>Maintenance</option><option>Installation</option><option>Emergency</option></select></div>
      <div class="full"><label for="m-msg">Equipment and issue</label><textarea id="m-msg" name="message" placeholder="Which equipment needs attention"></textarea></div>
      <div class="send"><button class="btn primary" type="submit">Schedule service</button> <a class="btn" href="tel:1800000000">Call now</a></div>
    </form>
  </section>

  <div class="photo tail" role="img" aria-label="Photo of two technicians discussing a tablet in a commercial kitchen"></div>

  <footer>
    <div class="brand"><i></i>HEARTHLINE</div>
    <div class="info">
      <b>Address</b>Level 2, 48 Harbour Lane, Sydney NSW 2000
      <b>Contact</b><a href="tel:1800000000">1800 000 000</a><a href="mailto:hello@hearthlineservice.com">hello@hearthlineservice.com</a>
    </div>
    <div class="socials"><span class="dot"></span><span class="dot"></span><span class="dot"></span><span class="dot"></span><span class="dot"></span></div>
    <ul><li>Services</li><li>Repair plans</li><li>Maintenance</li><li>Installation</li><li>Equipment sales</li></ul>
    <ul><li>Emergency support</li><li>About company</li><li>Our team</li><li>Careers</li><li>Contact us</li></ul>
    <div class="legal">Privacy policy<br>Terms of service<br>Cookies settings</div>
    <div class="copy">© 2024 Hearthline Kitchen Service. All rights reserved.</div>
  </footer>
</div>

</body>
</html>
```